Brisk Ember - Stock Certificate

We need a custom designed stock certificate that represents the look of our company logo but also have a cool look compared to a standard stock certificate. We thinking we want the logo in gold. Our website is https://www.briskemberusa.example.

We are wanting the certificate to look very professional and really cool, we have sales agents that work for the company and we are creating a program by which the sales agents can gain ownership in the company. So the certificates need to have a very cool appeal and that provides a sense of pride in owning "Units" in Brisk Ember.

Reason: Extending so other board members can vote as well, thank you all!

Target Market(s)

Stock/Shareholders

Industry/Entity Type

It Company

Font styles to use
Script

Requirements
Must have
• Must look like a stock certificate, must use our logo which the psd file for it was attached.
Nice to have
• Nice to have the logo in gold

```html
<!DOCTYPE html>
<html lang="en">
<head>
<meta charset="utf-8">
<title>Brisk Ember – Unit Ownership Certificate</title>
<link rel="stylesheet" href="https://fonts.googleapis.com/css2?family=Pinyon+Script&family=Quicksand:wght@500;600;700&display=swap">
<style>
  :root {
    --page: #d6d6d6;
    --paper-white: #ffffff;
    --band-peach: #fdd5a0;
    --band-tan: #d2b89a;
    --cream: #f7ebdf;
    --ink: #3a3a3c;
    --gold: #c29a3a;
  }
  html, body {
    margin: 0;
    width: 1200px;
    height: 1200px;
    overflow: hidden;
    background: var(--page);
  }
  .certificate {
    position: absolute;
    left: 52px;
    top: 213px;
    width: 1096px;
    height: 774px;
  }
  .certificate svg { display: block; width: 100%; height: 100%; }
  .title, .recipient { font-family: "Pinyon Script", cursive; fill: var(--ink); stroke: var(--ink); stroke-width: 1.2; }
  .lead, .body-copy, .signature-name, .signature-role, .seal-year, .brand-name {
    font-family: "Quicksand", sans-serif;
    fill: var(--ink);
  }
  .lead { font-weight: 500; }
  .body-copy { font-weight: 600; }
  .signature-name, .signature-role { font-weight: 600; }
  .seal-year { font-weight: 700; }
  .brand-name { font-weight: 700; fill: var(--gold); }
</style>
</head>
<body>
<div class="certificate">
  <svg viewBox="0 0 1370 968" preserveAspectRatio="none" xmlns="http://www.w3.org/2000/svg">
    <rect class="paper" width="1370" height="968" fill="var(--paper-white)"/>
    <polygon class="band-peach" points="0,0 700,55 1370,360 1370,968 0,968" fill="var(--band-peach)"/>
    <polygon class="band-tan" points="0,5 695,52 1370,428 1370,962 48,940" fill="var(--band-tan)"/>
    <polygon class="panel-cream" points="10,14 675,66 1370,440 1370,966 82,935" fill="var(--cream)"/>

    <g class="brand">
      <circle cx="1174" cy="118" r="16" fill="var(--gold)"/>
      <text class="brand-name" x="1174" y="190" font-size="19" text-anchor="middle">Brisk Ember</text>
    </g>

    <g class="seal">
      <rect x="1080" y="280" width="72" height="160" fill="var(--ink)"/>
      <polygon points="1013,624 1050,557 1073,572 1050,642 1040,608" fill="var(--ink)"/>
      <polygon points="1157,572 1185,557 1250,631 1213,624 1175,659" fill="var(--ink)"/>
      <circle cx="1117" cy="509" r="80" fill="var(--cream)"/>
      <circle cx="1117" cy="509" r="62" fill="none" stroke="var(--ink)" stroke-width="20"/>
      <text class="seal-year" x="1117" y="519" font-size="30" text-anchor="middle">2017</text>
    </g>

    <text class="title" x="168" y="342" font-size="132" textLength="428" lengthAdjust="spacingAndGlyphs">Certificate</text>
    <text class="lead" x="168" y="494" font-size="27">This certificate is presented to</text>
    <text class="recipient" x="168" y="602" font-size="96" textLength="445" lengthAdjust="spacingAndGlyphs">Name Surname</text>

    <g class="body-copy" font-size="17.5">
      <text x="168" y="663">Certificate No. 0017 – registered holder of One Hundred (100) Units.</text>
      <text x="168" y="684">These fully paid Units represent ownership in Brisk Ember and are transferable</text>
      <text x="168" y="705">only on the books of the company by the holder in person or by</text>
      <text x="168" y="728">duly authorized attorney.</text>
    </g>

    <g class="signature">
      <text class="signature-name" x="1129" y="780" font-size="19" text-anchor="middle">Name Here</text>
      <line x1="1033" y1="791" x2="1222" y2="791" stroke="var(--ink)" stroke-width="2" opacity="0.7"/>
      <text class="signature-role" x="1129" y="815" font-size="18" text-anchor="middle">Ownership</text>
    </g>
  </svg>
</div>
</body>
</html>
```